Refresh of graphic design for existing website

We would like to refresh our website. Please see the attached design specifications.

Industry/Entity Type

Graphic Design

```html
<!DOCTYPE html>
<html lang="en">
<head>
<meta charset="utf-8">
<title>Tool &amp; Machinery Alliance</title>
<link href="https://fonts.googleapis.com/css2?family=Open+Sans:wght@400;600;700&family=Noto+Serif:wght@400;700&display=swap" rel="stylesheet">
<style>
:root{
  --blue:#1c8ddb;
  --blue-dark:#126fb0;
  --nav:#2b2b2b;
  --nav-line:#3d3d3d;
  --ink:#333;
  --muted:#666;
  --footer:#262626;
  --footer-deep:#1b1b1b;
  --footer-text:#9a9a9a;
  --white:#fff;
  --rule:#e3e3e3;
}
*{box-sizing:border-box;margin:0;padding:0}
html,body{width:735px;height:1200px;overflow:hidden;background:var(--white)}
body{font-family:"Noto Serif",Georgia,serif;color:var(--ink);position:relative}
.sans{font-family:"Open Sans",Arial,sans-serif}

/* header */
.utility{position:absolute;right:0;top:0;height:20px;width:265px;background:var(--blue);
  font:600 9px "Open Sans",Arial,sans-serif;color:var(--white);display:flex;align-items:center;justify-content:center;gap:5px}
.brand{position:absolute;left:16px;top:24px;display:flex;align-items:center;gap:10px}
.brand-dot{width:46px;height:46px;border-radius:50%;background:var(--blue)}
.brand-name{font:700 40px/1 "Open Sans",Arial,sans-serif;color:var(--blue)}
.brand-sub{position:absolute;left:16px;top:92px;font:700 15px "Open Sans",Arial,sans-serif;color:#222}
.search{position:absolute;right:16px;top:76px;display:flex}
.search input{width:160px;height:24px;border:1px solid #ccc;border-right:0;background:var(--white);
  font:10px "Open Sans",Arial,sans-serif;padding:0 7px;color:var(--muted)}
.search button{height:24px;width:58px;border:0;background:var(--blue);color:var(--white);font:700 9px "Open Sans",Arial,sans-serif}

/* nav */
.nav{position:absolute;top:142px;left:0;width:735px;height:26px;background:var(--nav);display:flex;padding-left:14px}
.nav a{font:700 9.5px/26px "Open Sans",Arial,sans-serif;color:#ddd;text-decoration:none;padding:0 13px;letter-spacing:.3px;border-right:1px solid var(--nav-line)}
.nav a.active{background:#1f1f1f;color:var(--white);border-bottom:3px solid var(--blue);line-height:23px}

/* hero */
.hero{position:absolute;top:168px;left:0;width:735px;height:286px;
  background:linear-gradient(100deg,#2e3a48 0%,#6e7f90 30%,#c9d0d6 55%,#8a98a6 75%,#3a4655 100%)}
.hero-arrow{position:absolute;top:124px;width:26px;height:26px;border-radius:50%;background:rgba(0,0,0,.55)}
.hero-arrow.prev{left:10px}.hero-arrow.next{right:10px}
.hero-arrow svg{display:block;margin:7px auto}
.caption{position:absolute;right:34px;top:160px;width:240px;height:100px;background:rgba(20,20,20,.82);padding:10px 12px}
.caption h3{font:700 14px "Noto Serif",Georgia,serif;color:var(--blue);margin-bottom:6px}
.caption p{font:9px/1.45 "Noto Serif",Georgia,serif;color:#ddd}
.dots{position:absolute;left:16px;bottom:12px;display:flex;gap:6px}
.dots span{width:8px;height:8px;border-radius:50%;background:rgba(255,255,255,.5)}
.dots span.on{background:var(--blue)}

/* welcome */
.welcome{position:absolute;top:454px;left:0;width:735px;height:150px;text-align:center;padding-top:22px}
.welcome h1{font:700 17px "Noto Serif",Georgia,serif;color:#222;margin-bottom:12px}
.welcome p{width:530px;margin:0 auto;font:10px/1.6 "Noto Serif",Georgia,serif;color:var(--muted)}
.btn{display:inline-block;background:var(--blue);color:var(--white);font:600 10px "Open Sans",Arial,sans-serif;padding:8px 14px;border-radius:2px;margin-top:14px}

/* updates */
.updates{position:absolute;top:605px;left:14px;width:707px}
.updates h2{font:700 15px "Noto Serif",Georgia,serif;color:#222;padding-bottom:8px;border-bottom:1px solid var(--rule);margin-bottom:12px}
.cards{display:flex;gap:10px}
.card{width:169px}
.card .thumb{height:92px;margin-bottom:8px}
.card h4{font:700 11px "Noto Serif",Georgia,serif;color:#222;margin-bottom:4px}
.card p{font:8.5px/1.45 "Noto Serif",Georgia,serif;color:var(--muted);margin-bottom:4px}
.card .more{font:600 9px "Open Sans",Arial,sans-serif;color:var(--blue)}

/* footer */
.footer{position:absolute;top:860px;left:0;width:735px;height:305px;background:var(--footer);border-top:3px solid var(--blue)}
.to-top{position:absolute;left:336px;top:-22px}
.cols{display:flex;padding:40px 14px 0;gap:16px}
.col h5{font:700 9.5px "Open Sans",Arial,sans-serif;color:var(--white);letter-spacing:.4px;padding-bottom:7px;border-bottom:1px solid #3a3a3a;margin-bottom:10px}
.col p,.col li{font:8.5px/1.6 "Noto Serif",Georgia,serif;color:var(--footer-text)}
.col-company{width:160px}.col-blog{width:170px}.col-links{width:185px}.col-contact{width:130px}
.post{display:flex;gap:7px;margin-bottom:10px}
.post .pic{width:30px;height:30px;flex:none}
.links{list-style:none}
.links li{display:flex;align-items:center;gap:6px}
.links li::before{content:"";width:5px;height:5px;border-radius:50%;background:var(--blue);flex:none}
.field{height:20px;background:#333;border:1px solid #444;margin-bottom:7px;font:8.5px/18px "Open Sans",Arial,sans-serif;color:#888;padding-left:6px}
.field.tall{height:52px}
.submit{display:inline-block;background:var(--blue);color:var(--white);font:700 8.5px "Open Sans",Arial,sans-serif;padding:5px 9px}
.copyright{position:absolute;top:1165px;left:0;width:735px;height:35px;background:var(--footer-deep);
  font:8.5px/35px "Noto Serif",Georgia,serif;color:#777;padding-left:14px}
</style>
</head>
<body>

<header>
  <div class="utility">Sign Up <span>|</span> Login <span>|</span> RSS Feeds <span>|</span> Archived News</div>
  <div class="brand"><span class="brand-dot"></span><span class="brand-name">TMA</span></div>
  <div class="brand-sub">Tool &amp; Machinery Alliance</div>
  <form class="search"><input type="text" value="Search Our Website..."><button type="button">SEARCH</button></form>
</header>

<nav class="nav">
  <a class="active">HOME</a><a>ABOUT US</a><a>MEMBERSHIP</a><a>TMA MEMBERS</a><a>THE TMA LIBRARY</a><a>MARKET RESEARCH</a><a>HIDDEN FILES</a>
</nav>

<section class="hero" role="img" aria-label="Photo of a businessman in a suit touching a row of floating gear icons">
  <div class="hero-arrow prev"><svg width="10" height="12" viewBox="0 0 10 12"><path d="M7 1 2 6l5 5" stroke="#fff" stroke-width="2" fill="none"/></svg></div>
  <div class="hero-arrow next"><svg width="10" height="12" viewBox="0 0 10 12"><path d="M3 1l5 5-5 5" stroke="#fff" stroke-width="2" fill="none"/></svg></div>
  <div class="caption">
    <h3>Lorem ipsum dolor</h3>
    <p>Lorem ipsum dolor sit amet, consectetuer adipiscing elit, sed do eiusmod tempor incididunt ut labore et dolore magna aliqua. Ut enim ad minim veniam, quis nostrud exercitation ullamco.</p>
  </div>
  <div class="dots"><span class="on"></span><span></span><span></span><span></span></div>
</section>

<section class="welcome">
  <h1>Welcome to Tool &amp; Machinery Alliance</h1>
  <p>TMA is one of the most respected trade associations in the automotive aftermarket, giving fair and equitable representation to all segments of the equipment and tool industry. The Alliance is an association of automotive tool and equipment manufacturers and technical information providers and training organizations.</p>
  <span class="btn">Read More</span>
</section>

<section class="updates">
  <h2>Latest Updates</h2>
  <div class="cards">
    <article class="card">
      <div class="thumb" role="img" aria-label="Hand pointing at a cluster of industrial gear icons" style="background:linear-gradient(135deg,#dfe4e8,#9aa8b4)"></div>
      <h4>Industrial Events</h4>
      <p>Vestibulum ante ipsum primis in faucibus orci luctus et ultrices posuere cubilia curae donec velit.</p>
      <span class="more">Read More »</span>
    </article>
    <article class="card">
      <div class="thumb" role="img" aria-label="Breaking news graphic beside a man in a suit" style="background:linear-gradient(135deg,#c62828,#e9e9e9 60%,#8b8b8b)"></div>
      <h4>Breaking News</h4>
      <p>Vestibulum ante ipsum primis in faucibus orci luctus et ultrices posuere cubilia curae donec velit.</p>
      <span class="more">Read More »</span>
    </article>
    <article class="card">
      <div class="thumb" role="img" aria-label="Blue digital network of connected lines" style="background:linear-gradient(135deg,#0d2b55,#2f7fd0 60%,#0b1c38)"></div>
      <h4>Join TMA</h4>
      <p>Vestibulum ante ipsum primis in faucibus orci luctus et ultrices posuere cubilia curae donec velit.</p>
      <span class="more">Read More »</span>
    </article>
    <article class="card">
      <div class="thumb" role="img" aria-label="Two hands fitting puzzle pieces together" style="background:linear-gradient(135deg,#eef0e8,#b9c98a 60%,#8aa24c)"></div>
      <h4>Lorem Ipsum</h4>
      <p>Vestibulum ante ipsum primis in faucibus orci luctus et ultrices posuere cubilia curae donec velit.</p>
      <span class="more">Read More »</span>
    </article>
  </div>
</section>

<footer class="footer">
  <svg class="to-top" width="62" height="22" viewBox="0 0 62 22"><path d="M0 22 31 0l31 22H46L31 11 16 22z" fill="var(--blue)"/></svg>
  <div class="cols">
    <div class="col col-company">
      <h5>COMPANY DETAILS</h5>
      <p>Lorem ipsum dolor sit amet, consectetur adipiscing elit. Duis nec lacus velit vel fringilla mauris.</p>
      <p style="margin-top:8px">Company Name<br>Tool &amp; Machinery Alliance<br>1200 Harbor Street<br>Springfield, ST 00000<br>Tel: 000-000-0000<br>Fax: 000-000-0000<br>Email: info@example.org</p>
    </div>
    <div class="col col-blog">
      <h5>LATEST BLOG POSTS</h5>
      <div class="post"><div class="pic" role="img" aria-label="Blog post thumbnail photo" style="background:linear-gradient(135deg,#5a6672,#2d343b)"></div><p>Nulla in diam. Ut fringilla, consectetur lorem id nunc at tempus.</p></div>
      <div class="post"><div class="pic" role="img" aria-label="Blog post thumbnail photo" style="background:linear-gradient(135deg,#6b7580,#333b43)"></div><p>Nulla in diam. Ut fringilla, consectetur lorem id nunc at tempus.</p></div>
      <div class="post"><div class="pic" role="img" aria-label="Blog post thumbnail photo" style="background:linear-gradient(135deg,#59636d,#2a3037)"></div><p>Nulla in diam. Ut fringilla, consectetur lorem id nunc at tempus.</p></div>
    </div>
    <div class="col col-links">
      <h5>QUICK LINKS</h5>
      <ul class="links">
        <li>Lorem ipsum dolor sit</li>
        <li>Amet consectetur</li>
        <li>Praesent vel nisi id</li>
        <li>Curabitur tincidunt vel</li>
        <li>Aliquam eget erat nec sapien</li>
        <li>Duis id magna auctor</li>
        <li>In nec justo non</li>
        <li>Vivamus mollis metus ut</li>
      </ul>
    </div>
    <div class="col col-contact">
      <h5>CONTACT US</h5>
      <div class="field">Name</div>
      <div class="field">Email</div>
      <div class="field tall">Message</div>
      <span class="submit">SUBMIT</span>
    </div>
  </div>
</footer>
<div class="copyright">Copyright © 2014 Tool &amp; Machinery Alliance | All Rights Reserved</div>

</body>
</html>
```